Broschüre KTR Festival
Zielgruppe
Wir sind ein Verband, der Ensembles der Amateurmusik (Blasorchester, Chöre, Akkordeonensembles ....) vertritt. Unsere Zielgruppe sind Menschen, die in ihrer Freizeit musizieren ebenso, wie Menschen die gerne Konzerte besuchen.
Die Broschüre ist ein Programmheft für ein eintägiges Festival mit mehreren Open-Air Bühnen.
Aufgabenstellung
Die Broschüre sollte DIN lang Format sein, damit sie gut in die Westentasche passt. Zentraler Bestandteil neben den Textseiten sind die Termintabellen, die die Auftritte auf den Bühnen abbilden.

```html
<!DOCTYPE html>
<html lang="de">
<head>
<meta charset="utf-8">
<title>KTR Festival – Programmheft</title>
<link href="https://fonts.googleapis.com/css2?family=Ubuntu:wght@700&family=Oswald:wght@300&family=Open+Sans:wght@400&display=swap" rel="stylesheet">
<style>
  :root {
    --teal: #1b9a8c;
    --paper: #ffffff;
    --divider: #807e7f;
    --wreath-a: #f39a1e;
    --wreath-b: #d9245e;
    --wreath-c: #1f9c98;
    --wreath-d: #8e2f7c;
    --wreath-e: #c6d64a;
  }
  html, body {
    margin: 0;
    padding: 0;
    width: 1200px;
    height: 2400px;
    overflow: hidden;
    background: var(--divider);
  }
  .canvas {
    position: relative;
    width: 1200px;
    height: 2400px;
  }
  .page {
    position: absolute;
    left: 4px;
    width: 1172px;
    background: var(--paper);
    overflow: hidden;
  }
  .page--cover { top: 0; height: 1173px; }
  .page--program { top: 1195px; height: 1205px; }
  .wreath {
    position: absolute;
    left: 0;
    top: 0;
  }
  .frame-line {
    position: absolute;
    border: 9px solid var(--paper);
    box-sizing: border-box;
  }
  .panel {
    position: absolute;
    background: var(--paper);
  }
  .brand {
    position: absolute;
    left: 566px;
    top: 560px;
    font-family: "Ubuntu", sans-serif;
    font-weight: 700;
    color: var(--teal);
    font-size: 58px;
    line-height: 1.02;
    margin: 0;
  }
  .brand__meta {
    position: absolute;
    left: 570px;
    top: 724px;
    font-family: "Ubuntu", sans-serif;
    font-weight: 700;
    color: var(--teal);
    font-size: 35px;
    line-height: 1.12;
    margin: 0;
  }
  .program {
    position: absolute;
    left: 366px;
    top: 347px;
    color: var(--teal);
    margin: 0;
  }
  .program__title {
    font-family: "Open Sans", sans-serif;
    font-weight: 400;
    font-size: 39px;
    letter-spacing: 0.5px;
    margin: 0 0 8px 0;
    line-height: 52px;
  }
  .program__list {
    list-style: none;
    margin: 0;
    padding: 0;
    font-family: "Oswald", sans-serif;
    font-weight: 300;
    font-size: 35px;
    line-height: 58.5px;
  }
  .program__more {
    position: absolute;
    left: 366px;
    top: 768px;
    color: var(--teal);
    margin: 0;
  }
  .program__more-label {
    font-family: "Oswald", sans-serif;
    font-weight: 300;
    font-size: 27px;
    line-height: 40px;
    display: block;
  }
  .program__more-url {
    font-family: "Open Sans", sans-serif;
    font-size: 37px;
    line-height: 56px;
    display: block;
  }
</style>
</head>
<body>
<div class="canvas">

  <section class="page page--cover">
    <svg class="wreath" width="1172" height="1173" role="img" aria-label="Kranz aus bunten, polygonal gestalteten Musikinstrumenten: Trommel, Trompete, Lautsprecher, Gitarren, Keyboard, Plattenspieler, Kopfhörer und Saxofon">
      <defs>
        <linearGradient id="wreathCover" x1="0" y1="0" x2="1" y2="1">
          <stop offset="0" stop-color="var(--wreath-b)"/>
          <stop offset="0.3" stop-color="var(--wreath-a)"/>
          <stop offset="0.55" stop-color="var(--wreath-c)"/>
          <stop offset="0.8" stop-color="var(--wreath-d)"/>
          <stop offset="1" stop-color="var(--wreath-e)"/>
        </linearGradient>
      </defs>
      <ellipse cx="585" cy="600" rx="545" ry="545" fill="url(#wreathCover)" opacity="0.85"/>
    </svg>
    <div class="frame-line" style="left:294px; top:322px; width:584px; height:586px;"></div>
    <div class="panel" style="left:322px; top:355px; width:522px; height:524px;"></div>
    <p class="brand">KTR<br>Festival</p>
    <p class="brand__meta">11.07.2020<br>Seeburg</p>
  </section>

  <section class="page page--program">
    <svg class="wreath" width="1172" height="1205" role="img" aria-label="Kranz aus bunten, polygonal gestalteten Musikinstrumenten rund um das Programm">
      <defs>
        <linearGradient id="wreathProgram" x1="0" y1="0" x2="1" y2="1">
          <stop offset="0" stop-color="var(--wreath-b)"/>
          <stop offset="0.3" stop-color="var(--wreath-a)"/>
          <stop offset="0.55" stop-color="var(--wreath-c)"/>
          <stop offset="0.8" stop-color="var(--wreath-d)"/>
          <stop offset="1" stop-color="var(--wreath-e)"/>
        </linearGradient>
      </defs>
      <ellipse cx="585" cy="600" rx="545" ry="548" fill="url(#wreathProgram)" opacity="0.85"/>
    </svg>
    <div class="frame-line" style="left:294px; top:324px; width:584px; height:566px;"></div>
    <div class="panel" style="left:322px; top:346px; width:850px; height:518px;"></div>
    <div class="program">
      <h2 class="program__title">PROGRAMM</h2>
      <ul class="program__list">
        <li>10 Uhr Eröffnung Bühne I</li>
        <li>Eröffnungsveranstaltung mit Sternmarsch</li>
        <li>10 bis 17 Uhr&nbsp; Musik auf allen Bühnen</li>
        <li>11 Uhr Verleihung der Konrad-Kessler-Tafel</li>
        <li>17 Uhr Schlusskonzert Bühne I</li>
      </ul>
    </div>
    <p class="program__more">
      <span class="program__more-label">Weitere Informationen:</span>
      <span class="program__more-url">www.ktr-festival.de</span>
    </p>
  </section>

</div>
</body>
</html>
```